Bravik = Difficult

Sto Je Treba Ni Bravik
what must be done, is not difficult...

my mom is Croatian and her name is Marela.

a Croatian expression that I came across 12 years ago is 'what must be done, is not difficult'. yes, it is counter-intuitive. but it helped me to get divorced and then to beat Stage 4 cancer. both seem impossible,

but they they had to be done, so they were not difficult.

so I have started up a new company called:
Bravik Consulting - solving difficult

I'll be working with companies that have a difficult program/project that they haven't launched yet...

I envision possibly a business card that is shaped into a "D" to represent the Croatian word of difficult.

yes, I know this is difficult - welcome to my new world - the difficult challenges are worth solving...

a nod to the red/white design of the Croatian flag would be nice.

```html
<!DOCTYPE html>
<html lang="en">
<head>
<meta charset="utf-8">
<title>Bravik Consulting – Business Card</title>
<link rel="stylesheet" href="https://fonts.googleapis.com/css2?family=Grandstander:ital,wght@0,800;1,700;1,800&family=Lato:wght@400&display=swap">
<style>
  :root {
    --brand-red: #e2001a;
    --ink: #111111;
    --paper: #ffffff;
  }
  * { margin: 0; padding: 0; box-sizing: border-box; }
  html, body {
    width: 1200px;
    height: 898px;
    overflow: hidden;
    background: var(--paper);
  }
  .canvas {
    position: relative;
    width: 1200px;
    height: 898px;
  }

  /* Front side */
  .card-front {
    position: absolute;
    left: 106px;
    top: 206px;
    width: 458px;
    height: 456px;
    background: var(--brand-red);
    display: flex;
    align-items: center;
    justify-content: center;
  }
  .card-front .maze-field {
    position: absolute;
    inset: 0;
    background: var(--brand-red);
  }
  .front-name {
    position: relative;
    font-family: "Grandstander", "Trebuchet MS", sans-serif;
    font-weight: 800;
    font-size: 68px;
    line-height: 1.05;
    color: var(--paper);
    text-align: center;
  }

  /* Back side */
  .card-back {
    position: absolute;
    left: 630px;
    top: 203px;
    width: 459px;
    height: 459px;
    background: var(--paper);
    border: 2px solid var(--brand-red);
    overflow: hidden;
  }
  .back-header {
    position: absolute;
    top: 36px;
    left: 0;
    right: 0;
    text-align: center;
    color: var(--brand-red);
    font-family: "Grandstander", "Trebuchet MS", sans-serif;
    font-style: italic;
  }
  .company-name {
    font-size: 30px;
    font-weight: 800;
    line-height: 34px;
  }
  .tagline {
    font-size: 22px;
    font-weight: 700;
    line-height: 28px;
  }
  .contact-list {
    position: absolute;
    top: 116px;
    left: 0;
    right: 0;
    list-style: none;
    text-align: center;
    font-family: "Grandstander", "Trebuchet MS", sans-serif;
    font-style: italic;
    font-weight: 700;
    font-size: 24px;
    line-height: 31.5px;
    color: var(--ink);
  }
  .website {
    position: absolute;
    top: 255px;
    left: 69px;
    font-family: "Grandstander", "Trebuchet MS", sans-serif;
    font-weight: 800;
    font-size: 24px;
    color: var(--ink);
  }
  .motto {
    position: absolute;
    top: 301px;
    left: 69px;
    font-family: "Lato", "Gill Sans", sans-serif;
    font-size: 19px;
    line-height: 28px;
    color: var(--ink);
  }
  .corner-stripes {
    position: absolute;
    left: 0;
    bottom: 0;
    width: 459px;
    height: 200px;
  }
</style>
</head>
<body>
<main class="canvas">

  <section class="card-front" aria-label="Card front">
    <div class="maze-field" role="img" aria-label="Red field with a white square maze pattern"></div>
    <p class="front-name">Bravik<br>consulting</p>
  </section>

  <section class="card-back" aria-label="Card back">
    <header class="back-header">
      <h1 class="company-name">Bravik Consulting</h1>
      <p class="tagline">solving difficult</p>
    </header>

    <ul class="contact-list">
      <li>Name Surname Surname</li>
      <li>info@bravik.com</li>
      <li>+00 00 00 00 00</li>
      <li>+00 00 00 00 00</li>
    </ul>

    <p class="website">www.bravikconsulting.com</p>

    <p class="motto">“What must be done,<br>is not difficult”.</p>

    <svg class="corner-stripes" viewBox="0 0 459 200" role="img" aria-label="Red diagonal maze stripe pattern in the corner">
      <polygon points="0,200 459,0 459,200" fill="var(--brand-red)"/>
    </svg>
  </section>

</main>
</body>
</html>
```